Business Card Design Project

We're looking for a unique business card design that stands out from the rest, using the brand and logo we've already developed.
Two-sided design please.
Brightvane Media (www.brightvanemedia.com.au) is a digitally-focused advertising agency that has produces results-driven campaigns. As a result, we'd like our business card to reflect our innovative approach.
Size, shape, orientation, etc, are all flexible (providing the print costs don't become ridiculous or we have to sit there with tiny scissors!).
Business card should include space for name, title, email, mobile, landline and address.
Logo files uploaded.

```html
<!DOCTYPE html>
<html lang="en">
<head>
<meta charset="utf-8">
<title>Brightvane Media — Business Card</title>
<link href="https://fonts.googleapis.com/css2?family=Barlow:wght@300;400&display=swap" rel="stylesheet">
<style>
  :root {
    --backdrop: #e9e7e3;
    --brand-orange: #d97323;
    --card-white: #ededec;
    --ink: #3a3a3a;
    --ink-soft: #555555;
  }
  * { box-sizing: border-box; margin: 0; padding: 0; }
  html, body {
    width: 1200px;
    height: 900px;
    overflow: hidden;
    background: var(--backdrop);
    font-family: "Barlow", Arial, sans-serif;
  }
  .canvas {
    width: 1200px;
    height: 900px;
    display: flex;
    align-items: center;
    justify-content: center;
    gap: 80px;
  }
  .card {
    width: 380px;
    height: 665px;
    padding: 56px 44px 48px;
    display: flex;
    flex-direction: column;
    box-shadow: 0 4px 14px rgba(0,0,0,0.12);
  }
  .card--front { background: var(--brand-orange); }
  .card--back { background: var(--card-white); }

  .wordmark {
    display: flex;
    align-items: center;
    gap: 10px;
    font-weight: 300;
    font-size: 30px;
    line-height: 1.1;
    letter-spacing: 0.5px;
    color: var(--ink);
  }
  .wordmark__dot {
    flex: none;
    width: 14px;
    height: 14px;
    border-radius: 50%;
    background: var(--ink);
  }
  .card--back .wordmark__dot { background: var(--brand-orange); }

  .contact {
    margin-top: 90px;
    color: var(--ink);
  }
  .contact__name {
    font-size: 22px;
    font-weight: 400;
    line-height: 1.15;
  }
  .contact__title {
    font-size: 14px;
    font-weight: 400;
    color: var(--ink-soft);
    margin-top: 4px;
  }
  .contact__lines {
    list-style: none;
    margin-top: 40px;
    font-size: 14px;
    line-height: 1.5;
    font-weight: 300;
  }
  .contact__label {
    display: inline-block;
    width: 20px;
    font-weight: 400;
  }
  .contact__address {
    margin-top: 36px;
    font-size: 14px;
    line-height: 1.5;
    font-weight: 300;
    font-style: normal;
  }
  .contact__web {
    margin-top: 48px;
    font-size: 14px;
    color: var(--brand-orange);
    font-weight: 400;
  }
</style>
</head>
<body>
<main class="canvas">
  <section class="card card--front" aria-label="Card front">
    <div class="wordmark"><span class="wordmark__dot"></span>Brightvane Media</div>
  </section>

  <section class="card card--back" aria-label="Card back">
    <div class="wordmark"><span class="wordmark__dot"></span>Brightvane Media</div>
    <div class="contact">
      <p class="contact__name">Mara Lindqvist</p>
      <p class="contact__title">Operation Manager</p>
      <ul class="contact__lines">
        <li><span class="contact__label">T</span>1300 555 208</li>
        <li><span class="contact__label">M</span>(221) 55 410 38 92</li>
        <li><span class="contact__label">E</span>name@brightvanemedia.com.au</li>
      </ul>
      <address class="contact__address">4/27 Harbourline St,<br>Kelvin, Qld, 4102</address>
      <p class="contact__web">www.brightvanemedia.com.au</p>
    </div>
  </section>
</main>
</body>
</html>
```